Ward Compass Business Card Design*

We need a business card design for our company Ward Compass. Our company is specialized in providing online consulting services regarding medical institutions, hospitals and doctors. We work with patients worldwide looking to choose between healthcare providers. We have a website you may use as a reference, where we list doctors and clinics worldwide. So we target Medical providers as well as patients worldwide.
Target Market(s)
Medical Providers and patients around the world
Industry/Entity Type
Medical
Contact Information for Business Card
Salma Driouch
CEO
+90 612 348 2751
info@wardcompass.example
www.wardcompass.example
17 Essafsaf 3 H.Q.L. Rabat, Morocco
Requirements
Must have
- Company logo/name on one full side, personal info and smaller logo and company name on the other side.
Nice to have
- Smart and elegant design

```html
<!DOCTYPE html>
<html lang="en">
<head>
<meta charset="utf-8">
<title>Ward Compass – Business Card</title>
<link href="https://fonts.googleapis.com/css2?family=Lato:wght@400;700&family=Montserrat:wght@600&display=swap" rel="stylesheet">
<style>
  :root {
    --navy: #13365f;
    --grey: #8a8a8c;
    --light-grey: #f1f1f1;
    --paper: #ffffff;
    --ink: #333333;
    --backdrop: #d9d9d7;
  }
  * { box-sizing: border-box; margin: 0; padding: 0; }
  html, body { width: 1200px; height: 801px; overflow: hidden; }
  body {
    background: var(--backdrop);
    font-family: "Lato", sans-serif;
    position: relative;
  }
  .card {
    position: absolute;
    top: 246px;
    width: 540px;
    height: 309px;
    overflow: hidden;
    box-shadow: 0 6px 18px rgba(0,0,0,0.18);
  }
  .card-front { left: 50px; background: var(--paper); }
  .card-back { left: 610px; background: var(--navy); }

  .front-shapes { position: absolute; inset: 0; }

  .wordmark {
    position: absolute;
    display: flex;
    align-items: center;
    font-family: "Montserrat", sans-serif;
    font-weight: 600;
    text-transform: uppercase;
    letter-spacing: 1px;
    white-space: nowrap;
  }
  .wordmark-dot { border-radius: 50%; flex: none; }
  .card-front .wordmark { left: 34px; top: 92px; font-size: 24px; color: var(--navy); gap: 12px; }
  .card-front .wordmark-dot { width: 40px; height: 40px; background: var(--navy); }

  .person { position: absolute; right: 46px; top: 92px; text-align: right; }
  .person-name { font-weight: 700; font-size: 20px; color: var(--navy); line-height: 1.1; }
  .person-role { font-size: 13px; color: var(--ink); margin-top: 2px; }

  .divider { position: absolute; left: 36px; right: 40px; top: 150px; height: 1px; background: var(--navy); }

  .contact-list { position: absolute; left: 36px; top: 164px; list-style: none; font-size: 13px; color: var(--ink); }
  .contact-list li { display: flex; align-items: center; gap: 8px; line-height: 20px; }
  .contact-list svg { width: 11px; height: 11px; fill: var(--navy); flex: none; }

  .address { position: absolute; right: 46px; top: 164px; text-align: right; font-size: 13px; line-height: 19px; color: var(--ink); }

  .front-web { position: absolute; right: 40px; bottom: 34px; font-size: 12px; color: var(--paper); letter-spacing: 0.3px; }

  .card-back .wordmark { left: 50%; top: 118px; transform: translateX(-50%); font-size: 34px; color: var(--paper); gap: 16px; }
  .card-back .wordmark-dot { width: 56px; height: 56px; background: var(--grey); }
  .back-web { position: absolute; left: 0; right: 0; top: 214px; text-align: center; font-size: 15px; color: var(--paper); letter-spacing: 1px; }
</style>
</head>
<body>
  <section class="card card-front" aria-label="Business card front">
    <svg class="front-shapes" viewBox="0 0 540 309" preserveAspectRatio="none" aria-hidden="true">
      <circle cx="330" cy="58" r="68" fill="none" stroke="var(--light-grey)" stroke-width="22"/>
      <path d="M0 262 L300 262 C325 262 330 240 355 236 L540 236 L540 309 L0 309 Z" fill="var(--grey)" opacity="0.9"/>
      <path d="M0 274 L300 274 C330 274 335 232 365 226 L540 226 L540 309 L0 309 Z" fill="var(--navy)"/>
      <rect x="0" y="288" width="540" height="21" fill="var(--navy)"/>
      <rect x="0" y="281" width="540" height="4" fill="var(--light-grey)" opacity="0.0"/>
    </svg>

    <div class="wordmark"><span class="wordmark-dot"></span>Ward Compass</div>

    <div class="person">
      <p class="person-name">Salma Driouch</p>
      <p class="person-role">CEO</p>
    </div>

    <div class="divider"></div>

    <ul class="contact-list">
      <li><svg viewBox="0 0 24 24"><path d="M6.6 10.8a15.1 15.1 0 0 0 6.6 6.6l2.2-2.2c.3-.3.7-.4 1-.2 1.1.4 2.3.6 3.6.6.6 0 1 .4 1 1V20c0 .6-.4 1-1 1C10.6 21 3 13.4 3 4c0-.6.4-1 1-1h3.5c.6 0 1 .4 1 1 0 1.3.2 2.5.6 3.6.1.3 0 .7-.2 1z"/></svg>+90 612 348 2751</li>
      <li><svg viewBox="0 0 24 24"><path d="M2 5h20v14H2z M2 5l10 8 10-8" fill="var(--navy)"/></svg>info@wardcompass.example</li>
    </ul>

    <p class="address">17 Essafsaf 3<br>H.Q.L. Rabat, Morocco</p>

    <p class="front-web">www.wardcompass.example</p>
  </section>

  <section class="card card-back" aria-label="Business card back">
    <div class="wordmark"><span class="wordmark-dot"></span>Ward Compass</div>
    <p class="back-web">www.wardcompass.example</p>
  </section>
</body>
</html>
```